Flyer for Clothing Line Launch Event

I need a flyer designed for the launch of my women's clothing line in February 2016. I will need to use this flyer on my website, social media and print.

The Collections

Our contemporary collections are comprised of influences drawing from bohemian and chic motifs. The term "Bohemian" is described as "simply an artist or littérateur who, consciously or unconsciously, secedes from conventionality in life and in art". "Chic" was borrowed from the French in the late 19th century and has come to mean stylish or elegant.

About my company:

We design free and romantic garments targeted to fashion-forward women driven by uniqueness and desire to accentuate her confidence and class through style. We look forward to our clients indulging in the LorettaVance brand to include our Keystone Circle, Lend-A-Heart, eNewsletters, Trunk Shows and Fashion Shows.

Target Market(s)

upscale women ages 30-50

Industry/Entity Type

Fashion

Font styles to use
Decorative
Script
Other font styles liked:
• Handwritten type script

Colors
000000
f37122
3377b5
e667a6

Requirements
Must have
• colors similar to my website boutique.lorettavance-example.com
• my logo
Nice to have
• image from my website
• my logo

```html
<!DOCTYPE html>
<html lang="en">
<head>
<meta charset="utf-8">
<title>LorettaVance Boutique – Collection Launch Soiree</title>
<link rel="stylesheet" href="https://fonts.googleapis.com/css2?family=Great+Vibes&family=Oswald:wght@400;500;600&family=Open+Sans:wght@400;600;700&display=swap">
<style>
  :root {
    --ink: #0b0b0b;
    --ink-soft: #1c1c1c;
    --orange: #f37122;
    --pink: #e667a6;
    --pink-deep: #d94691;
    --white: #ffffff;
    --grey: #6a6a6a;
    --page: #d9d9d9;
  }
  * { margin: 0; padding: 0; box-sizing: border-box; }
  html, body { width: 863px; height: 1200px; overflow: hidden; background: var(--page); }
  .flyer {
    position: relative; width: 863px; height: 1200px; overflow: hidden;
    background: var(--ink); font-family: "Open Sans", sans-serif; color: var(--white);
  }
  .portrait {
    position: absolute; top: 0; right: 0; width: 450px; height: 620px;
    background: radial-gradient(ellipse at 55% 40%, #c9a58c 0%, #7d5a48 35%, #2a1d18 70%, #0b0b0b 100%);
  }
  .brand {
    position: absolute; top: 46px; left: 70px; display: flex; align-items: center; gap: 12px;
  }
  .brand-dot { width: 26px; height: 26px; border-radius: 50%; background: var(--pink); }
  .brand-name {
    font-family: "Oswald", sans-serif; font-weight: 500; font-size: 26px; letter-spacing: 3px; color: var(--pink);
  }
  .intro { position: absolute; top: 150px; left: 40px; width: 380px; text-align: center; }
  .intro-label { font-family: "Oswald", sans-serif; font-size: 19px; letter-spacing: 2px; }
  .intro-title { font-family: "Great Vibes", cursive; font-size: 44px; color: var(--pink); margin-top: 4px; line-height: 1.1; }
  .intro-join { font-family: "Oswald", sans-serif; font-size: 24px; letter-spacing: 2px; margin-top: 8px; }
  .designer-box {
    margin: 14px auto 0; width: 340px; padding: 10px 0 12px; background: var(--pink-deep);
    border-radius: 4px;
  }
  .designer-box .name { font-family: "Oswald", sans-serif; font-weight: 600; font-size: 25px; }
  .designer-box .sub { font-size: 17px; margin-top: 2px; }
  .event-shape { position: absolute; left: 0; top: 500px; width: 863px; height: 400px; }
  .event { position: absolute; top: 640px; left: 0; width: 863px; text-align: center; }
  .event-title { font-family: "Oswald", sans-serif; font-weight: 500; font-size: 52px; color: var(--pink-deep); letter-spacing: 1px; }
  .event-sub { font-family: "Oswald", sans-serif; font-size: 34px; color: var(--grey); margin-top: 2px; }
  .event-date {
    display: inline-block; margin-top: 14px; padding: 6px 44px; background: var(--orange); border-radius: 24px;
    font-family: "Oswald", sans-serif; font-weight: 500; font-size: 30px; letter-spacing: 3px;
  }
  .info { position: absolute; top: 880px; left: 60px; right: 60px; display: flex; gap: 60px; }
  .info-col { flex: 1; }
  .info-col h2 {
    font-family: "Oswald", sans-serif; font-weight: 500; font-size: 16px; letter-spacing: 1px; color: var(--orange);
    padding-bottom: 6px; border-bottom: 1px solid #333; margin-bottom: 10px;
  }
  .info-col p { font-size: 12px; line-height: 1.5; color: #cfcfcf; }
  .footer {
    position: absolute; left: 0; bottom: 0; width: 863px; height: 70px; background: var(--pink-deep);
    display: flex; align-items: center; justify-content: space-between; padding: 0 60px;
    font-size: 14px;
  }
  .follow { display: flex; align-items: center; gap: 8px; }
  .social { width: 22px; height: 22px; border-radius: 4px; background: var(--white); }
</style>
</head>
<body>
<main class="flyer">
  <div class="portrait" role="img" aria-label="Portrait photo of a woman with curly dark hair wearing a soft fur collar"></div>

  <div class="brand">
    <span class="brand-dot"></span>
    <span class="brand-name">LORETTAVANCE</span>
  </div>

  <section class="intro">
    <p class="intro-label">INTRODUCING</p>
    <p class="intro-title">LorettaVance Boutique</p>
    <p class="intro-join">PLEASE JOIN</p>
    <div class="designer-box">
      <p class="name">Designer Loretta Vance</p>
      <p class="sub">for her Collection Launch Soiree</p>
    </div>
  </section>

  <svg class="event-shape" viewBox="0 0 863 400" aria-hidden="true">
    <path d="M0 300 Q200 330 330 360 L0 380 Z" fill="var(--pink-deep)"/>
    <path d="M0 120 L300 120 Q400 120 431.5 30 Q463 120 563 120 L863 120 L863 270 L563 270 Q463 270 431.5 380 Q400 270 300 270 L0 270 Z" fill="var(--orange)"/>
    <path d="M0 130 L300 130 Q398 130 431.5 42 Q465 130 563 130 L863 130 L863 262 L563 262 Q461 262 431.5 366 Q402 262 300 262 L0 262 Z" fill="var(--white)"/>
  </svg>

  <section class="event">
    <h1 class="event-title">RUNWAY SHOW SHOPPING</h1>
    <p class="event-sub">Lite Bites &amp; Champaign</p>
    <p class="event-date">FEBRUARY 20, 2016</p>
  </section>

  <section class="info">
    <div class="info-col">
      <h2>ABOUT MY COMPANY</h2>
      <p>We design free and romantic garments targeted to fashion-forward women driven by uniqueness and desire to accentuate her confidence and class through style. We look forward to our clients indulging in the LorettaVance brand to include our Keystone Circle, Lend-A-Heart, eNewsletters, Trunk Shows and Fashion Shows.</p>
    </div>
    <div class="info-col">
      <h2>THE COLLECTIONS</h2>
      <p>Our contemporary collections are comprised of influences drawing from bohemian and chic motifs. The term "Bohemian" is described as "simply an artist or littérateur who, consciously or unconsciously, secedes from conventionality in life and in art". "Chic" was borrowed from the French in the late 19th century and has come to mean stylish or elegant.</p>
    </div>
  </section>

  <footer class="footer">
    <span class="site">boutique.lorettavance-example.com</span>
    <span class="follow">Follow us at <span class="social"></span><span class="social"></span><span class="social"></span></span>
  </footer>
</main>
</body>
</html>
```